PowerPoint Template Design for business consulting company in Silicon Valley

I need a PowerPoint template to use as the starting point for new presentations. I have a logo but now need design that supports this. I've attached a very descriptive PDF that explains exactly what I need. Here is a list of deliverables: 1. PowerPoint Template that I will use as the starter presentation for all new Lantern Quorix presentationsDesigns for the following slides: See picture below for examples of structure:2. Title slide with subtitle3. Section header4. Title and body5. Title and 2 columns6. Title and 3 columns7. One column text8. Editable timeline to show months, or steps for a process9. Bullet design for unordered list (can be graphic)10. Bullet design for ordered list11. Recommended fonts for each design: Title, subtitle, list, captionOPTIONAL: Possible graphic elements to be used for section title slide backgrounds or graphic elements:--Your team / my team / people on project--Goals for project / presentation--Editable Timeline--Speaking--Writing--Listening--People collaborating / helping each otherI am happy to accept proposals for developing these optional elements in a separate project.

Requirements
Must have
• Must be FLAT design.
• Not flashy or garish. Must be subtle.

```html
<!DOCTYPE html>
<html lang="en">
<head>
<meta charset="utf-8">
<title>Lantern Quorix — Presentation Template</title>
<link rel="stylesheet" href="https://fonts.googleapis.com/css2?family=Montserrat:wght@400;600;700;800&family=Open+Sans:wght@400;600&display=swap">
<style>
  :root {
    --blue: #3d7ff0;
    --blue-deep: #2b63d6;
    --green: #3fd0a0;
    --navy: #2a3350;
    --ink: #3c4358;
    --muted: #9aa1b2;
    --line: #e4e8ef;
    --paper: #ffffff;
    --canvas: #f1f3f6;
    --gold: #d8c27a;
    --chart-dark: #2f3b52;
  }
  * { box-sizing: border-box; margin: 0; padding: 0; }
  html, body { width: 826px; height: 1200px; overflow: hidden; }
  body { background: var(--canvas); font-family: "Open Sans", Arial, sans-serif; color: var(--ink); position: relative; }

  .slide { position: absolute; width: 394px; height: 222px; background: var(--paper); overflow: hidden; box-shadow: 0 1px 3px rgba(30,40,60,.12); }
  .col-a { left: 14px; } .col-b { left: 418px; }
  .row-1 { top: 21px; } .row-2 { top: 255px; } .row-3 { top: 489px; } .row-4 { top: 723px; } .row-5 { top: 957px; }

  .slide-title { font-family: "Montserrat", Arial, sans-serif; font-weight: 700; color: var(--navy); font-size: 13px; text-align: center; position: absolute; left: 0; right: 0; top: 16px; }
  .title-rule { position: absolute; left: 50%; top: 36px; width: 30px; height: 2px; margin-left: -15px; background: var(--blue); }
  .small { font-size: 5px; line-height: 1.5; color: var(--muted); }
  .label { font-family: "Montserrat", Arial, sans-serif; font-weight: 700; font-size: 6px; color: var(--navy); }

  .brand { position: absolute; top: 8px; right: 10px; display: flex; align-items: center; gap: 3px; }
  .brand-dot { width: 9px; height: 9px; border-radius: 50%; background: var(--green); }
  .brand-name { font-family: "Montserrat", Arial, sans-serif; font-weight: 700; font-size: 6px; color: var(--navy); }
  .page-dot { position: absolute; left: 8px; bottom: 8px; width: 6px; height: 6px; border-radius: 50%; background: var(--green); }

  /* 1 title */
  .cover-photo { position: absolute; inset: 0; background: linear-gradient(160deg, #49607d 0%, #2a3854 55%, #1b2438 100%); }
  .cover-shade { position: absolute; left: 0; top: 0; bottom: 0; width: 62%; background: linear-gradient(90deg, rgba(20,28,46,.85), rgba(20,28,46,0)); }
  .cover-text { position: absolute; left: 22px; top: 62px; color: #fff; }
  .cover-kicker { font-family: "Montserrat", Arial, sans-serif; font-weight: 600; font-size: 12px; letter-spacing: 1px; }
  .cover-head { font-family: "Montserrat", Arial, sans-serif; font-weight: 800; font-size: 17px; letter-spacing: .5px; margin-top: 2px; }
  .cover-sub { font-size: 5px; color: #c9d1df; margin-top: 6px; width: 150px; line-height: 1.5; }
  .cover-btn { display: inline-block; margin-top: 10px; border: 1px solid #fff; font-size: 5px; padding: 3px 8px; font-weight: 600; letter-spacing: .5px; }

  /* 2 strategy */
  .strategy-body { position: absolute; left: 22px; top: 62px; width: 200px; }
  .strategy-body h2 { font-family: "Montserrat", Arial, sans-serif; font-size: 13px; color: var(--navy); position: absolute; top: -46px; }
  .strategy-body h3 { font-family: "Montserrat", Arial, sans-serif; font-size: 7px; color: var(--navy); margin-bottom: 5px; }
  .stat-panel { position: absolute; right: 0; top: 0; bottom: 0; width: 142px; background: var(--blue); color: #fff; padding: 30px 22px; }
  .stat { display: flex; align-items: center; justify-content: space-between; margin-bottom: 34px; }
  .stat-icon { width: 16px; height: 16px; border: 1.2px solid #fff; border-radius: 3px; }
  .stat-name { font-size: 5px; opacity: .85; }
  .stat-value { font-family: "Montserrat", Arial, sans-serif; font-weight: 700; font-size: 18px; text-align: right; }

  /* 3 steps */
  .frame-gold { position: absolute; inset: 6px; border: 1px solid var(--gold); }
  .step-text { position: absolute; width: 60px; text-align: center; }

  /* 4 strategy chart */
  .strategy-list { position: absolute; left: 24px; top: 50px; }
  .strategy-item { display: flex; gap: 6px; margin-bottom: 14px; width: 130px; }
  .item-icon { width: 14px; height: 14px; border-radius: 50%; flex: none; }

  /* 5 table */
  .market-table { position: absolute; left: 26px; right: 26px; top: 50px; border-collapse: collapse; font-size: 5px; }
  .market-table th { background: var(--blue); color: #fff; font-weight: 600; padding: 5px 3px; }
  .market-table td { padding: 5px 3px; text-align: center; color: var(--muted); border-bottom: 1px solid var(--line); }
  .market-table tr:nth-child(even) td { background: #f6f8fb; }

  /* 6 team */
  .team { position: absolute; left: 40px; right: 40px; top: 54px; display: flex; justify-content: space-between; }
  .member { width: 80px; text-align: center; }
  .member-photo { width: 58px; height: 58px; border-radius: 50%; margin: 0 auto 6px; background: linear-gradient(150deg, #c9cdd6, #8e96a6); border: 3px solid #fff; box-shadow: 0 0 0 1px var(--line); }
  .member-role { font-size: 5px; color: var(--blue); margin: 1px 0 4px; }
  .socials { display: flex; justify-content: center; gap: 3px; }
  .socials span { width: 7px; height: 7px; border-radius: 50%; background: var(--blue); }
  .socials span:nth-child(2) { background: var(--green); }

  /* 7 market */
  .share { position: absolute; top: 92px; text-align: center; width: 90px; }
  .share-value { font-family: "Montserrat", Arial, sans-serif; font-weight: 600; font-size: 22px; color: var(--navy); }
  .share-label { font-family: "Montserrat", Arial, sans-serif; font-weight: 700; font-size: 7px; color: var(--navy); letter-spacing: 1px; }
  .market-core { position: absolute; left: 147px; top: 58px; width: 100px; height: 100px; border-radius: 50%; background: #dfe9fd; display: flex; align-items: center; justify-content: center; }
  .market-core-inner { width: 74px; height: 74px; border-radius: 50%; background: var(--blue); color: #fff; text-align: center; padding-top: 20px; }
  .market-core-inner b { font-family: "Montserrat", Arial, sans-serif; font-size: 17px; display: block; }
  .market-core-inner span { font-size: 5px; letter-spacing: 1px; }
  .market-caption { position: absolute; left: 137px; width: 120px; top: 164px; text-align: center; }

  /* 8 hexagons */
  .hex-captions { position: absolute; left: 20px; right: 20px; top: 150px; display: flex; justify-content: space-between; }
  .hex-caption { width: 62px; text-align: center; }

  /* 9 infographic */
  .info-items { position: absolute; left: 206px; top: 58px; display: grid; grid-template-columns: 80px 80px; gap: 20px 10px; }
  .info-item { display: flex; gap: 5px; }

  /* 10 sales */
  .sales-photo { position: absolute; left: 0; top: 0; width: 394px; height: 60px; background: linear-gradient(180deg, #eef1f5, #ffffff); }
  .vs { position: absolute; left: 182px; top: 118px; font-family: "Montserrat", Arial, sans-serif; font-weight: 800; font-size: 14px; color: var(--navy); width: 30px; text-align: center; }
</style>
</head>
<body>

<!-- 1 Title slide -->
<section class="slide col-a row-1">
  <div class="cover-photo" role="img" aria-label="Photo of a pagoda below a snow-capped mountain at dusk"></div>
  <div class="cover-shade"></div>
  <div class="cover-text">
    <div class="cover-kicker">WELCOME</div>
    <div class="cover-head">BUSINESS PRESENTATION</div>
    <p class="cover-sub">A clear starting point for every new client story and proposal.</p>
    <span class="cover-btn">READ MORE</span>
  </div>
</section>

<!-- 2 Title and body -->
<section class="slide col-b row-1">
  <div class="strategy-body">
    <h2>The Strategy</h2>
    <h3>Write Your Title Here</h3>
    <p class="small">Use this space to describe the main idea of the section. Keep sentences short and focused so the audience can follow the argument with ease. Support each point with a clear fact or a simple example drawn from the project.</p>
    <p class="small" style="margin-top:5px">Add a second paragraph for detail, next steps or a brief summary of the expected outcome.</p>
  </div>
  <div class="stat-panel">
    <div class="stat"><div><div class="stat-icon"></div><div class="stat-name" style="margin-top:3px">Growth</div></div><div class="stat-value">85%</div></div>
    <div class="stat"><div><div class="stat-icon"></div><div class="stat-name" style="margin-top:3px">Reach</div></div><div class="stat-value">46%</div></div>
  </div>
</section>

<!-- 3 Timeline -->
<section class="slide col-a row-2">
  <div class="frame-gold"></div>
  <div class="brand"><span class="brand-dot"></span><span class="brand-name">Lantern Quorix</span></div>
  <div class="slide-title">5 Steps to launch a program</div>
  <svg width="394" height="222" style="position:absolute;left:0;top:0">
    <path d="M62 118 C80 88, 110 88, 128 118 S176 148, 196 118 S244 88, 264 118 S312 148, 332 118" fill="none" stroke="#d7def0" stroke-width="6"/>
    <g stroke-width="5" fill="#fff">
      <circle cx="62" cy="118" r="20" stroke="var(--blue)"/>
      <circle cx="129" cy="118" r="20" stroke="var(--green)"/>
      <circle cx="196" cy="118" r="20" stroke="var(--blue)"/>
      <circle cx="263" cy="118" r="20" stroke="var(--green)"/>
      <circle cx="332" cy="118" r="20" stroke="var(--blue)"/>
    </g>
    <g font-family="Montserrat, Arial, sans-serif" font-weight="700" font-size="9" fill="#2a3350" text-anchor="middle">
      <text x="62" y="121">01</text><text x="129" y="121">02</text><text x="196" y="121">03</text><text x="263" y="121">04</text><text x="332" y="121">05</text>
    </g>
  </svg>
  <div class="step-text" style="left:99px;top:56px"><div class="label">Insert Title Here</div><p class="small">Short note on this step</p></div>
  <div class="step-text" style="left:233px;top:56px"><div class="label">Insert Title Here</div><p class="small">Short note on this step</p></div>
  <div class="step-text" style="left:32px;top:150px"><div class="label">Insert Title Here</div><p class="small">Short note on this step</p></div>
  <div class="step-text" style="left:166px;top:150px"><div class="label">Insert Title Here</div><p class="small">Short note on this step</p></div>
  <div class="step-text" style="left:302px;top:150px"><div class="label">Insert Title Here</div><p class="small">Short note on this step</p></div>
  <div class="page-dot"></div>
</section>

<!-- 4 Strategy chart -->
<section class="slide col-b row-2">
  <div class="brand"><span class="brand-dot"></span><span class="brand-name">Lantern Quorix</span></div>
  <div class="slide-title" style="left:170px;text-align:left">The Strategy</div>
  <div class="strategy-list">
    <div class="strategy-item"><span class="item-icon" style="background:var(--blue)"></span><div><div class="label">Step One</div><p class="small">Define goals and scope clearly</p></div></div>
    <div class="strategy-item"><span class="item-icon" style="background:var(--green)"></span><div><div class="label">Marketing Value</div><p class="small">Shape the offer for each market</p></div></div>
    <div class="strategy-item"><span class="item-icon" style="background:var(--chart-dark)"></span><div><div class="label">Step Three</div><p class="small">Measure and refine the results</p></div></div>
  </div>
  <svg width="220" height="120" viewBox="0 0 220 120" style="position:absolute;left:160px;top:60px">
    <polygon points="0,120 0,70 40,40 80,75 120,30 160,60 200,20 220,40 220,120" fill="var(--chart-dark)"/>
    <polygon points="0,120 0,85 45,60 90,90 130,55 175,85 220,60 220,120" fill="var(--green)"/>
    <polygon points="0,120 0,100 50,85 95,105 140,80 185,100 220,90 220,120" fill="var(--blue)"/>
  </svg>
  <div class="page-dot"></div>
</section>

<!-- 5 Table -->
<section class="slide col-a row-3">
  <div class="brand"><span class="brand-dot"></span><span class="brand-name">Lantern Quorix</span></div>
  <div class="slide-title">Market Size Comparation</div>
  <div class="title-rule"></div>
  <table class="market-table">
    <thead><tr><th>Region</th><th>2019</th><th>2020</th><th>2021</th><th>2022</th><th>2023</th></tr></thead>
    <tbody>
      <tr><td>North</td><td>120</td><td>134</td><td>150</td><td>162</td><td>178</td></tr>
      <tr><td>South</td><td>98</td><td>104</td><td>117</td><td>125</td><td>139</td></tr>
      <tr><td>East</td><td>76</td><td>82</td><td>91</td><td>99</td><td>108</td></tr>
      <tr><td>West</td><td>143</td><td>151</td><td>166</td><td>180</td><td>192</td></tr>
      <tr><td>Central</td><td>64</td><td>70</td><td>77</td><td>85</td><td>94</td></tr>
    </tbody>
  </table>
  <div class="page-dot"></div>
</section>

<!-- 6 Team -->
<section class="slide col-b row-3">
  <div class="brand"><span class="brand-dot"></span><span class="brand-name">Lantern Quorix</span></div>
  <div class="slide-title">The Team</div>
  <div class="title-rule"></div>
  <div class="team">
    <div class="member"><div class="member-photo" role="img" aria-label="Portrait photo of a team member"></div><div class="label">Iris Vale</div><div class="member-role">Lead Consultant</div><div class="socials"><span></span><span></span><span></span></div></div>
    <div class="member"><div class="member-photo" role="img" aria-label="Portrait photo of a team member"></div><div class="label">Tomas Reed</div><div class="member-role">Strategy Advisor</div><div class="socials"><span></span><span></span><span></span></div></div>
    <div class="member"><div class="member-photo" role="img" aria-label="Portrait photo of a team member"></div><div class="label">Nina Hollis</div><div class="member-role">Project Manager</div><div class="socials"><span></span><span></span><span></span></div></div>
  </div>
  <div class="page-dot"></div>
</section>

<!-- 7 Market share -->
<section class="slide col-a row-4">
  <div class="brand"><span class="brand-dot"></span><span class="brand-name">Lantern Quorix</span></div>
  <div class="slide-title">Market Size Comparation</div>
  <div class="title-rule"></div>
  <div class="share" style="left:28px"><div class="share-value">67%</div><div class="share-label">HUMANS</div></div>
  <div class="market-core"><div class="market-core-inner"><b>$186</b><span>BILLION</span></div></div>
  <div class="market-caption"><div class="label">Total Available Market</div><p class="small">Estimated value across all segments</p></div>
  <div class="share" style="right:28px"><div class="share-value">33%</div><div class="share-label">ROBOTS</div></div>
  <div class="page-dot"></div>
</section>

<!-- 8 Hexagons -->
<section class="slide col-b row-4">
  <div class="brand"><span class="brand-dot"></span><span class="brand-name">Lantern Quorix</span></div>
  <div class="slide-title">Title headline goes here</div>
  <div class="title-rule"></div>
  <svg width="394" height="100" viewBox="0 0 394 100" style="position:absolute;left:0;top:58px">
    <g stroke="var(--blue)" stroke-width="1.5">
      <polygon points="51,20 77,35 77,65 51,80 25,65 25,35" fill="#fff"/>
      <polygon points="124,20 150,35 150,65 124,80 98,65 98,35" fill="var(--blue)"/>
      <polygon points="197,20 223,35 223,65 197,80 171,65 171,35" fill="#fff"/>
      <polygon points="270,20 296,35 296,65 270,80 244,65 244,35" fill="var(--blue)"/>
      <polygon points="343,20 369,35 369,65 343,80 317,65 317,35" fill="#fff"/>
    </g>
    <g fill="none" stroke-width="1.5">
      <circle cx="51" cy="50" r="6" stroke="var(--blue)"/><circle cx="124" cy="50" r="6" stroke="#fff"/>
      <circle cx="197" cy="50" r="6" stroke="var(--blue)"/><circle cx="270" cy="50" r="6" stroke="#fff"/>
      <circle cx="343" cy="50" r="6" stroke="var(--blue)"/>
    </g>
  </svg>
  <div class="hex-captions">
    <div class="hex-caption"><div class="label">Headline 1</div><p class="small">Brief line of detail</p></div>
    <div class="hex-caption"><div class="label">Headline 2</div><p class="small">Brief line of detail</p></div>
    <div class="hex-caption"><div class="label">Headline 3</div><p class="small">Brief line of detail</p></div>
    <div class="hex-caption"><div class="label">Headline 4</div><p class="small">Brief line of detail</p></div>
    <div class="hex-caption"><div class="label">Headline 5</div><p class="small">Brief line of detail</p></div>
  </div>
  <div class="page-dot"></div>
</section>

<!-- 9 Infographic -->
<section class="slide col-a row-5">
  <div class="brand"><span class="brand-dot"></span><span class="brand-name">Lantern Quorix</span></div>
  <div class="slide-title" style="right:180px">Business Infographic</div>
  <div class="title-rule" style="left:107px"></div>
  <svg width="170" height="130" viewBox="0 0 170 130" style="position:absolute;left:24px;top:54px">
    <g stroke="#e4e8ef" stroke-width="1">
      <line x1="10" y1="10" x2="165" y2="10"/><line x1="10" y1="40" x2="165" y2="40"/>
      <line x1="10" y1="70" x2="165" y2="70"/><line x1="10" y1="100" x2="165" y2="100"/>
      <line x1="10" y1="120" x2="165" y2="120" stroke="#c7ccd6"/>
    </g>
    <polyline points="10,90 40,30 70,60 100,85 130,50 160,70" fill="none" stroke="var(--blue)" stroke-width="2"/>
    <polyline points="10,60 40,80 70,35 100,55 130,95 160,40" fill="none" stroke="var(--green)" stroke-width="2"/>
    <polyline points="10,105 40,95 70,100 100,70 130,80 160,100" fill="none" stroke="var(--chart-dark)" stroke-width="1.5"/>
  </svg>
  <div class="info-items">
    <div class="info-item"><span class="item-icon" style="background:var(--blue)"></span><div><div class="label">Vision</div><p class="small">Where we aim to go next</p></div></div>
    <div class="info-item"><span class="item-icon" style="background:var(--green)"></span><div><div class="label">Research</div><p class="small">Facts that guide choices</p></div></div>
    <div class="info-item"><span class="item-icon" style="background:var(--green)"></span><div><div class="label">Planning</div><p class="small">Steps, owners and dates</p></div></div>
    <div class="info-item"><span class="item-icon" style="background:var(--blue)"></span><div><div class="label">Delivery</div><p class="small">Results shared with clients</p></div></div>
  </div>
  <div class="page-dot"></div>
</section>

<!-- 10 Sales report -->
<section class="slide col-b row-5">
  <div class="sales-photo" role="img" aria-label="Faded photo of a city skyline"></div>
  <div class="brand"><span class="brand-dot"></span><span class="brand-name">Lantern Quorix</span></div>
  <div class="slide-title">Sales Report</div>
  <div class="title-rule"></div>
  <svg width="394" height="150" viewBox="0 0 394 150" style="position:absolute;left:0;top:52px">
    <g>
      <rect x="30" y="20" width="16" height="110" fill="#e9edf3"/><rect x="30" y="50" width="16" height="80" fill="var(--blue)"/>
      <rect x="54" y="20" width="16" height="110" fill="#e9edf3"/><rect x="54" y="35" width="16" height="95" fill="var(--green)"/>
      <rect x="78" y="20" width="16" height="110" fill="#e9edf3"/><rect x="78" y="60" width="16" height="70" fill="var(--chart-dark)"/>
      <rect x="102" y="20" width="16" height="110" fill="#e9edf3"/><rect x="102" y="45" width="16" height="85" fill="var(--blue)"/>
      <rect x="126" y="20" width="16" height="110" fill="#e9edf3"/><rect x="126" y="30" width="16" height="100" fill="var(--green)"/>
      <rect x="150" y="20" width="16" height="110" fill="#e9edf3"/><rect x="150" y="70" width="16" height="60" fill="var(--blue)"/>

      <rect x="228" y="20" width="16" height="110" fill="#e9edf3"/><rect x="228" y="40" width="16" height="90" fill="var(--green)"/>
      <rect x="252" y="20" width="16" height="110" fill="#e9edf3"/><rect x="252" y="55" width="16" height="75" fill="var(--blue)"/>
      <rect x="276" y="20" width="16" height="110" fill="#e9edf3"/><rect x="276" y="30" width="16" height="100" fill="var(--chart-dark)"/>
      <rect x="300" y="20" width="16" height="110" fill="#e9edf3"/><rect x="300" y="65" width="16" height="65" fill="var(--green)"/>
      <rect x="324" y="20" width="16" height="110" fill="#e9edf3"/><rect x="324" y="45" width="16" height="85" fill="var(--blue)"/>
      <rect x="348" y="20" width="16" height="110" fill="#e9edf3"/><rect x="348" y="35" width="16" height="95" fill="var(--green)"/>
    </g>
    <g font-family="Open Sans, Arial, sans-serif" font-size="5" fill="#9aa1b2" text-anchor="middle">
      <text x="98" y="140">2022 Sales</text><text x="296" y="140">2023 Sales</text>
    </g>
  </svg>
  <div class="vs">VS</div>
  <div class="page-dot"></div>
</section>

</body>
</html>
```